Trendy Interior Design Company Postcard

We're looking to create a 4x6 or 5x7 double sided postcard type of flyer with our Logo on the front and some photos and information on the back. We would like it to capture peoples attention and to communicate that we are a trendy interior design/build company that can take on a diverse variety of projects to suit any type of client.
We have many more photos of projects, if needed.

Target Market(s)

High end residential home renovations and builds.

Industry/Entity Type

It Company

Font styles to use
Serif
Sans Serif

Requirements
Must have
• Our logo on the front, and on the back we want a variety of photos of our jobs, We would like our company contact information: 555-238-9047 - info@quorvel.ca and something to entice potential clients to contact us, such as " Call for your quote today"
Nice to have
• Diversity in designs. As many photos as possible without looking too busy. We want it to look clean, sleek, and neat. Colours should match our website and logo.
Should not have
• Too much colour. No tacky/unprofessional looking fonts.

```html
<!DOCTYPE html>
<html lang="en">
<head>
<meta charset="utf-8">
<title>Quorvel Homes — Postcard Back</title>
<link href="https://fonts.googleapis.com/css2?family=League+Spartan:wght@600;700&family=Hind:wght@400;500&display=swap" rel="stylesheet">
<style>
  :root {
    --page: #d9d9d6;
    --card: #f2f2f1;
    --cell-light: #e8e9e7;
    --cell-soft: #f4f4f3;
    --ink: #2d2a26;
    --dark: #2a2b29;
    --on-dark: #f1f1ef;
    --accent: #e2bd67;
    --photo-a: #9a9794;
    --photo-b: #4a4744;
    --photo-c: #c9c6c0;
  }
  * { box-sizing: border-box; margin: 0; padding: 0; }
  html, body { width: 1200px; height: 1200px; overflow: hidden; background: var(--page); }
  .postcard {
    position: absolute; left: 40px; top: 226px;
    width: 1273px; height: 850px;
    transform: scale(0.88); transform-origin: 0 0;
    background: var(--card);
    font-family: "Hind", sans-serif; color: var(--ink);
  }
  .block { position: absolute; display: flex; align-items: center; justify-content: center; text-align: center; }
  .brand { left: 60px; top: 60px; width: 150px; height: 90px; gap: 12px; justify-content: flex-start; }
  .brand-square { width: 22px; height: 22px; background: var(--ink); flex: none; }
  .brand-name { font-size: 30px; font-weight: 500; color: var(--ink); }
  .headline {
    position: absolute; left: 243px; top: 44px;
    font-family: "League Spartan", sans-serif; font-weight: 700;
    font-size: 50px; line-height: 62px; letter-spacing: -0.5px; color: var(--ink);
  }
  .cta { left: 844px; top: 25px; width: 200px; height: 171px; background: var(--cell-light); font-size: 15px; line-height: 23px; }
  .contact { left: 1044px; top: 25px; width: 204px; height: 171px; background: var(--dark); color: var(--on-dark); flex-direction: column; }
  .contact-phone { font-size: 20px; margin-bottom: 8px; }
  .contact-line { font-size: 12px; line-height: 25px; }
  .photo { position: absolute; }
  .photo-kitchen { left: 24px; top: 196px; width: 815px; height: 506px;
    background: linear-gradient(160deg, var(--photo-c) 0%, var(--photo-a) 40%, var(--photo-b) 100%); }
  .photo-dining { left: 839px; top: 196px; width: 409px; height: 335px;
    background: linear-gradient(200deg, #d8d6d2 0%, #a49a8e 50%, #6b6560 100%); }
  .stage-label { font-size: 22px; background: var(--cell-soft); }
  .plan { left: 24px; top: 196px; width: 204px; height: 168px; }
  .design { left: 228px; top: 531px; width: 205px; height: 171px; background: var(--cell-light); }
  .build { left: 1044px; top: 531px; width: 204px; height: 171px; background: var(--cell-light); }
  .style-note { font-size: 14px; background: var(--cell-soft); }
  .modern { left: 839px; top: 531px; width: 205px; height: 171px; }
  .classic { left: 1044px; top: 702px; width: 204px; height: 124px; }
  .slogan { left: 635px; top: 196px; width: 204px; height: 168px; background: var(--dark); color: var(--on-dark);
    font-family: "League Spartan", sans-serif; font-weight: 600; font-size: 20px; line-height: 35px; text-transform: uppercase; }
  .promise { left: 635px; top: 364px; width: 409px; height: 167px; background: var(--accent);
    justify-content: flex-start; text-align: left; padding: 0 28px;
    font-family: "League Spartan", sans-serif; font-weight: 600; font-size: 20px; line-height: 32px; color: var(--ink); }
  .address { left: 26px; top: 702px; width: 202px; height: 124px; background: var(--dark); color: var(--on-dark); font-size: 15px; line-height: 21px; }
  .social { left: 228px; top: 702px; width: 205px; height: 124px; flex-direction: column; font-size: 14px; }
  .social-tags { font-size: 8px; margin-top: 6px; }
  .story { left: 433px; top: 702px; width: 611px; height: 120px; background: var(--cell-light);
    justify-content: flex-start; text-align: left; padding: 0 28px; font-size: 13.5px; line-height: 24px; }
</style>
</head>
<body>
  <main class="postcard">
    <div class="block brand"><span class="brand-square"></span><span class="brand-name">Quorvel</span></div>
    <h1 class="headline">The interior design of<br>Quorvel Homes</h1>

    <div class="block cta">Call for your quote<br>today</div>
    <div class="block contact">
      <div class="contact-phone">555-238-9047</div>
      <div class="contact-line">E-mail: info@quorvel.ca</div>
      <div class="contact-line">www.quorvel.ca</div>
    </div>

    <div class="photo photo-kitchen" role="img" aria-label="Photo of a modern open kitchen with island, bar stools, pendant lights and a glass dining table"></div>
    <div class="photo photo-dining" role="img" aria-label="Photo of a bright kitchen with long white island, set places and drum pendant lamps"></div>

    <div class="block stage-label plan">Plan</div>
    <div class="block stage-label design">Design</div>
    <div class="block stage-label build">Build</div>

    <div class="block slogan">From design<br>project to<br>execution</div>
    <div class="block promise">We’ll guide you through the maze of styles and possibilities. Together, we’ll choose how to make it both attractive and functional.</div>

    <div class="block style-note modern">Modern style</div>
    <div class="block style-note classic">Classic style</div>

    <div class="block address">48 Linden Ct,<br>Toronto, Ontario<br>M4C2R9</div>
    <div class="block social">
      <div>Find us on social media</div>
      <div class="social-tags">.pinboard .roomly .buildrate</div>
    </div>
    <div class="block story">Every new Quorvel Homes project begins with… a cup of fragrant tea or invigorating coffee. So, while talking about it, we choose among the variety of paths and options the one and only which satisfy all the client’s wishes.</div>
  </main>
</body>
</html>
```